Selvin: A Friday night in the Prophetic Flyer

We are holding 2 Friday night events, one on 10/25/19 and the other on 11/29/19.
The time frame is 6:30pm-9:00pm. These services will be a time of prayer/healing for the sick and will be prophetic as well. (There will be prophets prophesying over people)

The event is called: Selvin: A Friday night in the Prophetic
The flyer should also include the phrase/excerpt: "And they prophesied also".

Keywords/Phrases: Prophetic, Healing, Climbing in the Spirit, Higher level of Anointing...

Target Market(s)

those looking for healing, seeking a word from God

Colors

Designer to choose colors to be used in the design.

Requirements
Must have
• The event is called: Selvin: A Friday night in the Prophetic
• The flyer should also include the phrase/excerpt: "And they prophesied also".
• It must include the Tovik logo attached, either is fine, we have attached two different versions.
• It must have the dates, location, time
• Dates: October 25, 2019 and November 29, 2019
• Location: Hollard Community Center
• (Downtown Portland) 482 Wendle Street
• Portland, ME 04102
• Time: 6:30pm-9:00pm
• Contact Info: Tel. 207-555-3841
• email: contact@brimfield-hall.org
• web: www.tovik.org
Nice to have
• creativity in color scheme, the meaning of the word Selvin conveyed in a classy artistic way/design.
Should not have
• Crosses, pictures of churches

```html
<!DOCTYPE html>
<html lang="en">
<head>
<meta charset="utf-8">
<title>Selvin: A Friday night in the Prophetic</title>
<link rel="stylesheet" href="https://fonts.googleapis.com/css2?family=Archivo+Black&family=Cormorant+Garamond:ital,wght@0,500;1,600&family=Montserrat:wght@600&family=Oswald:wght@500&family=Orbitron:wght@500&display=swap">
<style>
  :root {
    --navy: #0f2a6b;
    --orange: #f6890f;
    --gold: #d9ae5c;
    --amber: #e88a32;
    --ember: #e0701f;
    --yellow: #f4ea1e;
    --white: #ffffff;
    --paper: #ffffff;
  }
  * { margin: 0; padding: 0; box-sizing: border-box; }
  html, body { width: 1000px; height: 1200px; overflow: hidden; background: var(--paper); }
  .flyer { position: relative; width: 1000px; height: 1200px; overflow: hidden; }
  .artwork { position: absolute; left: 37px; top: 0; width: 926px; height: 1200px; }
  .ripple-fill {
    position: absolute; left: 37px; top: 0; width: 926px; height: 1200px;
    background:
      radial-gradient(ellipse 520px 300px at 500px 760px, var(--ember) 0%, var(--amber) 40%, rgba(232,138,50,0) 75%),
      linear-gradient(180deg, var(--gold) 0%, #dfa24e 45%, var(--amber) 80%, #d98332 100%);
  }
  .brand {
    position: absolute; left: 95px; top: 82px;
    display: flex; align-items: center; gap: 10px;
    font-family: "Cormorant Garamond", serif; font-weight: 500;
    font-size: 44px; color: var(--white); letter-spacing: 1px;
  }
  .brand-dot { width: 14px; height: 14px; border-radius: 50%; background: var(--orange); }
  .keywords {
    position: absolute; top: 56px; left: 345px;
    display: flex; font-family: "Cormorant Garamond", serif; font-weight: 500;
    font-size: 31px; line-height: 38px; color: var(--white);
  }
  .keywords-left { text-align: right; padding-right: 12px; border-right: 2px solid var(--white); }
  .keywords-right { padding-left: 12px; }
  .quote {
    position: absolute; top: 478px; left: 0; width: 1000px; text-align: center;
    font-family: "Cormorant Garamond", serif; font-style: italic; font-weight: 600;
    font-size: 64px; line-height: 1; color: var(--navy); white-space: nowrap;
  }
  .quote-mark {
    position: absolute; font-family: Georgia, serif; font-weight: 700;
    font-size: 150px; line-height: 1; color: var(--navy);
  }
  .quote-open { left: 125px; top: 440px; }
  .quote-close { left: 815px; top: 505px; }
  .dates, .venue {
    position: absolute; left: 0; width: 1000px; text-align: center; white-space: nowrap;
    font-family: "Oswald", sans-serif; font-weight: 500; color: var(--white); text-transform: uppercase;
  }
  .dates { top: 615px; font-size: 29px; }
  .time {
    position: absolute; top: 704px; left: 0; width: 1000px; text-align: center;
    font-family: "Orbitron", sans-serif; font-weight: 500; font-size: 30px; color: var(--yellow);
  }
  .venue { top: 783px; font-size: 30px; line-height: 46px; }
  .contacts { position: absolute; left: 630px; top: 985px; list-style: none; }
  .contact {
    display: flex; align-items: flex-start; height: 57px;
    font-family: "Oswald", sans-serif; font-weight: 500; font-size: 19px; color: var(--yellow);
    text-transform: uppercase; white-space: nowrap;
  }
  .contact-icon {
    flex: none; width: 20px; height: 20px; border-radius: 50%; background: var(--yellow);
    display: flex; align-items: center; justify-content: center; margin-top: 2px;
  }
  .contact-text {
    margin-left: 5px; margin-top: 14px; min-width: 248px;
    border-bottom: 2px solid var(--yellow); padding-bottom: 1px; line-height: 24px;
  }
</style>
</head>
<body>
<main class="flyer">
  <div class="ripple-fill" role="img" aria-label="Golden liquid surface with a falling drop and concentric orange ripples"></div>

  <svg class="artwork" viewBox="37 0 926 1200" width="926" height="1200">
    <defs>
      <clipPath id="sky"><path d="M37 0 H963 V358 Q500 220 37 358 Z"/></clipPath>
      <clipPath id="surface"><path d="M37 358 Q500 220 963 358 V1200 H37 Z"/></clipPath>
    </defs>
    <path class="night-band" d="M37 0 H963 V358 Q500 220 37 358 Z" fill="var(--navy)"/>
    <g font-family="Archivo Black, sans-serif" font-size="222" text-anchor="middle">
      <text class="title-upper" x="505" y="346" textLength="632" lengthAdjust="spacingAndGlyphs" fill="var(--orange)" clip-path="url(#sky)">SELVIN</text>
      <text class="title-lower" x="505" y="346" textLength="632" lengthAdjust="spacingAndGlyphs" fill="var(--navy)" clip-path="url(#surface)">SELVIN</text>
    </g>
    <text class="subtitle" x="503" y="381" text-anchor="middle" textLength="630" lengthAdjust="spacingAndGlyphs"
      font-family="Montserrat, sans-serif" font-weight="600" font-size="27" fill="var(--navy)">A FRIDAY NIGHT IN THE PROPHETIC</text>
    <line x1="188" y1="384" x2="818" y2="384" stroke="var(--navy)" stroke-width="2"/>
  </svg>

  <div class="brand"><span class="brand-dot"></span>Tovik</div>

  <div class="keywords">
    <div class="keywords-left">Prophetic<br>Healing</div>
    <div class="keywords-right">Climbing in the Spirit<br>Higher level of Anointing</div>
  </div>

  <span class="quote-mark quote-open">“</span>
  <p class="quote">And they prophesied also</p>
  <span class="quote-mark quote-close">”</span>

  <p class="dates">October 25, 2019 &amp; November 29, 2019</p>
  <p class="time">6:30PM — 9:00PM</p>
  <p class="venue">Hollard Community Center<br>(Downtown Portland) 482 Wendle Street<br>Portland, ME 04102</p>

  <ul class="contacts">
    <li class="contact">
      <span class="contact-icon"><svg width="12" height="12" viewBox="0 0 24 24"><path d="M6.6 10.8a15 15 0 0 0 6.6 6.6l2.2-2.2c.3-.3.7-.4 1-.2 1.1.4 2.3.6 3.6.6.6 0 1 .4 1 1V20c0 .6-.4 1-1 1C10.6 21 3 13.4 3 4c0-.6.4-1 1-1h3.5c.6 0 1 .4 1 1 0 1.3.2 2.5.6 3.6.1.3 0 .7-.2 1z" fill="none" stroke="var(--ember)" stroke-width="2"/></svg></span>
      <span class="contact-text">207-555-3841</span>
    </li>
    <li class="contact">
      <span class="contact-icon"><svg width="12" height="12" viewBox="0 0 24 24"><rect x="3" y="5" width="18" height="14" fill="none" stroke="var(--ember)" stroke-width="2"/><path d="M3 5l9 8 9-8" fill="none" stroke="var(--ember)" stroke-width="2"/></svg></span>
      <span class="contact-text">contact@brimfield-hall.org</span>
    </li>
    <li class="contact">
      <span class="contact-icon"><svg width="12" height="12" viewBox="0 0 24 24"><circle cx="12" cy="12" r="9" fill="none" stroke="var(--ember)" stroke-width="2"/><ellipse cx="12" cy="12" rx="4" ry="9" fill="none" stroke="var(--ember)" stroke-width="2"/><path d="M3 12h18" stroke="var(--ember)" stroke-width="2"/></svg></span>
      <span class="contact-text">www.tovik.org</span>
    </li>
  </ul>
</main>
</body>
</html>
```